Criação de Papelaria Profissional para Consultoria de Negócios
A empresa queria:
" Consultoria em planejamento estratégico... marketing... aulas.. palestras.. artigos e livros publicados "

```html
<!DOCTYPE html>
<html lang="pt-BR">
<head>
<meta charset="UTF-8">
<title>Cartão de Visita – Leonardo Carvalho</title>
<link href="https://fonts.googleapis.com/css2?family=Open+Sans:wght@400;600&display=swap" rel="stylesheet">
<style>
  :root{
    --bg:#ecebe8;
    --card-light:#ffffff;
    --card-dark:#2b2b2b;
    --accent:#f2551d;
    --ink:#2a2a2a;
    --muted:#b5b5b5;
    --white:#ffffff;
  }
  *{margin:0;padding:0;box-sizing:border-box}
  html,body{width:1200px;height:1200px;overflow:hidden}
  body{background:var(--bg);font-family:"Open Sans",sans-serif;position:relative}

  .card{position:absolute;left:280px;width:640px;height:350px;overflow:hidden;
        box-shadow:0 6px 14px rgba(0,0,0,.18)}
  .card-front{top:230px;background:var(--card-light)}
  .card-back{top:640px;background:var(--card-dark)}
  .card-trim{position:absolute;inset:0;width:100%;height:100%}

  .brand{position:absolute;display:flex;align-items:center;gap:12px;
         font-weight:400;letter-spacing:1px;white-space:nowrap}
  .brand-dot{width:14px;height:14px;border-radius:50%;background:var(--accent);flex:none}
  .card-front .brand{left:50%;top:50%;transform:translate(-50%,-50%);
         font-size:30px;color:var(--ink)}
  .card-back .brand{right:42px;top:155px;font-size:24px;color:var(--white)}

  .holder{position:absolute;left:38px;top:62px;color:var(--white)}
  .holder-name{font-size:24px;font-weight:400}
  .holder-role{font-size:16px;color:var(--muted);margin-top:2px}

  .contact-list{position:absolute;left:38px;top:138px;list-style:none;
                color:var(--white);font-size:13px;line-height:1.45}
  .contact-item{display:flex;align-items:center;gap:14px;margin-bottom:16px}
  .contact-icon{width:26px;height:26px;border-radius:50%;background:var(--accent);
                display:flex;align-items:center;justify-content:center;flex:none}
  .contact-icon svg{width:14px;height:14px}
</style>
</head>
<body>

<section class="card card-front" aria-label="Frente do cartão">
  <svg class="card-trim" viewBox="0 0 640 350" preserveAspectRatio="none" aria-hidden="true">
    <rect x="250" y="0" width="330" height="4" fill="var(--accent)"/>
    <polygon points="500,0 640,0 640,10 510,10" fill="var(--ink)"/>
    <polygon points="0,340 150,340 160,350 0,350" fill="var(--ink)"/>
    <rect x="140" y="346" width="260" height="4" fill="var(--accent)"/>
  </svg>
  <div class="brand"><span class="brand-dot"></span>Leonardo Carvalho</div>
</section>

<section class="card card-back" aria-label="Verso do cartão">
  <svg class="card-trim" viewBox="0 0 640 350" preserveAspectRatio="none" aria-hidden="true">
    <polygon points="420,0 640,0 640,10 430,10" fill="var(--white)"/>
    <rect x="250" y="0" width="390" height="3" fill="var(--accent)"/>
    <polygon points="0,336 350,336 362,350 0,350" fill="var(--accent)"/>
    <polygon points="0,330 240,330 246,336 0,336" fill="var(--white)"/>
    <polygon points="430,340 640,340 640,350 420,350" fill="var(--white)"/>
  </svg>

  <div class="holder">
    <p class="holder-name">Nome Completo</p>
    <p class="holder-role">Cargo</p>
  </div>

  <ul class="contact-list">
    <li class="contact-item">
      <span class="contact-icon">
        <svg viewBox="0 0 16 16" fill="none" stroke="#fff" stroke-width="1.6"><rect x="1.5" y="3.5" width="13" height="9" rx="1"/><path d="M1.5 4l6.5 5 6.5-5"/></svg>
      </span>
      <span>Contato@exemplo.com<br>www.exemplo.com.br</span>
    </li>
    <li class="contact-item">
      <span class="contact-icon">
        <svg viewBox="0 0 16 16" fill="#fff"><path d="M3.5 1.5l2.5 0 1 3.5-1.8 1.2a8 8 0 0 0 4.6 4.6L11 9l3.5 1v2.5c0 1-1 2-2 2A11 11 0 0 1 1.5 3.5c0-1 1-2 2-2z"/></svg>
      </span>
      <span>(00) 9999-0000<br>(00) 9999-0000</span>
    </li>
    <li class="contact-item">
      <span class="contact-icon">
        <svg viewBox="0 0 16 16" fill="#fff"><path d="M8 1a5 5 0 0 0-5 5c0 3.8 5 9 5 9s5-5.2 5-9a5 5 0 0 0-5-5zm0 7a2 2 0 1 1 0-4 2 2 0 0 1 0 4z"/></svg>
      </span>
      <span>Rua exemplo, Rio de Janeiro - Rj</span>
    </li>
  </ul>

  <div class="brand"><span class="brand-dot"></span>Leonardo Carvalho</div>
</section>

</body>
</html>
```